DL Flyer Lantern Creek Hotel Thursday Night Bonus

We require a DL Portrait and landscape flyer for our Thursday Night Bonus Pull.
The way the draw works you must be part of our loyalty program, and on a Thursday night anytime between 5pm and 7pm, a name/number will be picked at random. If that person is in the hotel at the time they will win the jackpot.

The jackpot starts at $250 and goes up by $50 each week, if not won.

The things that the flyer must state:-
* loyalty program members only
* drawn on a Thursday night anytime between 5pm and 7pm
* QMRV/58/46271 must be written somewhere.
* see staff for details.
* our logo

Would like the flyer to be catch peoples attention but remain professional

If your unable to download logo, please forward email address and I will send it throuh

```html
<!DOCTYPE html>
<html lang="en">
<head>
<meta charset="utf-8">
<title>Lantern Creek Hotel – Thursday Night Bonus Pull</title>
<link rel="stylesheet" href="https://fonts.googleapis.com/css2?family=Tinos:wght@400;700&family=Questrial&display=swap">
<style>
  :root {
    --ink: #000000;
    --gold: #b8862f;
    --gold-light: #e0b45a;
    --red: #d3201b;
    --white: #ffffff;
    --bar-dark: #3a2a10;
  }
  * { margin: 0; padding: 0; box-sizing: border-box; }
  html, body { width: 1200px; height: 579px; overflow: hidden; background: var(--ink); }
  .flyer {
    position: relative;
    width: 1200px;
    height: 579px;
    background: var(--ink);
    font-family: "Tinos", "Times New Roman", serif;
    color: var(--white);
  }
  .brand {
    position: absolute;
    left: 88px;
    top: 82px;
    display: flex;
    align-items: center;
    gap: 18px;
  }
  .brand-mark {
    width: 70px;
    height: 70px;
    background: var(--gold);
  }
  .brand-name {
    font-weight: 400;
    font-size: 46px;
    line-height: 1;
    color: var(--gold-light);
    letter-spacing: 1px;
  }
  .photo-strip {
    position: absolute;
    left: 5px;
    top: 203px;
    display: flex;
    gap: 5px;
  }
  .photo { height: 174px; }
  .photo-grill { width: 202px; background: linear-gradient(135deg, #3a1a0e, #8a3a1a 45%, #e0782a 70%, #2a120a); }
  .photo-guitar { width: 204px; background: linear-gradient(120deg, #1a1410, #6a3a1c 40%, #c07a3a 60%, #2a1a12); }
  .photo-beer { width: 205px; background: radial-gradient(circle at 65% 45%, #c89a5a, #7a5028 45%, #2a1a0c); }
  .contact {
    position: absolute;
    left: 5px;
    width: 620px;
    top: 401px;
    text-align: center;
    color: var(--gold);
    font-style: normal;
    font-size: 20px;
    line-height: 31px;
  }
  .offer {
    position: absolute;
    left: 640px;
    width: 560px;
    top: 0;
    text-align: center;
  }
  .offer-program {
    margin-top: 40px;
    font-family: "Questrial", "Century Gothic", sans-serif;
    font-weight: 400;
    font-size: 56px;
    line-height: 60px;
    color: var(--gold);
  }
  .offer-members {
    margin-top: 3px;
    font-weight: 700;
    font-size: 33px;
    line-height: 38px;
    letter-spacing: 0.5px;
  }
  .offer-title {
    margin-top: 36px;
    font-weight: 700;
    font-size: 51px;
    line-height: 52px;
    color: var(--red);
  }
  .offer-start {
    margin-top: 27px;
    font-weight: 700;
    font-size: 33px;
    line-height: 38px;
    color: var(--gold);
  }
  .offer-terms {
    margin: 23px auto 0;
    width: 465px;
    font-size: 17px;
    line-height: 30px;
  }
  .cash-band {
    position: absolute;
    left: 0;
    top: 478px;
    width: 1200px;
    height: 101px;
    background: linear-gradient(180deg, #e8b83a, #d9a032 55%, #c9b878);
  }
  .licence-bar {
    position: absolute;
    left: 0;
    top: 528px;
    width: 1200px;
    height: 18px;
    background: linear-gradient(90deg, #8a6420, #e6c06a 30%, #b8862f 60%, #f0d080 85%, #9a7024);
  }
  .licence-text {
    position: absolute;
    left: 795px;
    top: 530px;
    font-size: 12.5px;
    line-height: 14px;
    color: var(--bar-dark);
  }
</style>
</head>
<body>
<main class="flyer">
  <div class="brand">
    <span class="brand-mark"></span>
    <span class="brand-name">Lantern Creek Hotel</span>
  </div>

  <div class="photo-strip">
    <div class="photo photo-grill" role="img" aria-label="Steaks cooking over a flaming grill"></div>
    <div class="photo photo-guitar" role="img" aria-label="Hands playing an acoustic guitar"></div>
    <div class="photo photo-beer" role="img" aria-label="Glasses of beer beside a wooden keg"></div>
  </div>

  <address class="contact">
    42 Wattle Street, Bellbrook, NSW 2999<br>
    Email: admin@lanterncreekhotel.net&nbsp; Phone: (02) 5550 1847
  </address>

  <section class="offer">
    <h2 class="offer-program">Loyalty Program</h2>
    <p class="offer-members">MEMBERS ONLY</p>
    <h1 class="offer-title">Thursday Night<br>Bonus Pull</h1>
    <p class="offer-start">STARTS AT $250.00</p>
    <p class="offer-terms">Drawn anytime between 5pm and 7pm. You MUST be in the hotel at the time of draw&nbsp; to be a winner. The prize will increase by $50.00 each week if not won.</p>
  </section>

  <div class="cash-band" role="img" aria-label="Scattered fifty dollar banknotes"></div>

  <div class="licence-bar"></div>
  <p class="licence-text">QMRV/58/46271 - see staff for details</p>
</main>
</body>
</html>
```